Online medical reviews website needs banner advert!

We need banner advert templates for our website, www.traineepanel.net. These should meet the technical requirements of our partner (uploaded).

Our groundbreaking website allows doctors in training to rate and review their training.

The adverts should use the same modern design language and colour scheme as our website. They should use the text 'Help a junior doctor make a big decision - rate your training!'.

Vector assets should be supplied, allowing us to use alternative text in future.
Updates

Industry/Entity Type

Healthcare

Font styles to use
Other font styles liked:
• Karla

Colors
3277b5
0555a3
ffffff

Requirements
Must have
• Similar design to our website. Should be elegant & modern. Must allow future text to be easily inserted.
Should not have
• Unrelated design.

```html
<!DOCTYPE html>
<html lang="en">
<head>
<meta charset="utf-8">
<title>Trainee Panel – Banner Set</title>
<link rel="stylesheet" href="https://fonts.googleapis.com/css2?family=Montserrat:wght@400;600&family=Bebas+Neue&display=swap">
<style>
  :root {
    --brand-blue: #0555a3;
    --brand-blue-light: #3277b5;
    --logo-navy: #1b2f86;
    --white: #ffffff;
    --stage: #e4e6e8;
    --rule: #d6d9dc;
    --photo-a: #c9b7a4;
    --photo-b: #6f87b3;
    --photo-c: #e8e4df;
  }
  * { box-sizing: border-box; margin: 0; padding: 0; }
  html, body { width: 1200px; height: 1200px; overflow: hidden; }
  body { background: var(--stage); font-family: "Montserrat", sans-serif; position: relative; }

  .banner { position: absolute; background: var(--brand-blue); overflow: hidden; color: var(--white); }
  .banner__header { position: absolute; left: 0; top: 0; background: var(--white); border-bottom: 2px solid var(--rule); }
  .banner__photo { position: absolute; background: linear-gradient(100deg, var(--photo-c) 0%, var(--photo-a) 35%, var(--photo-b) 75%, var(--photo-c) 100%); }
  .banner__swoosh { position: absolute; left: 0; top: 0; width: 100%; height: 100%; }
  .banner__swoosh path { fill: var(--brand-blue); }

  .logo { position: absolute; display: flex; align-items: center; gap: 8px; color: var(--logo-navy); font-family: "Montserrat", sans-serif; font-weight: 400; white-space: nowrap; letter-spacing: -0.5px; }
  .logo__mark { display: inline-block; background: var(--brand-blue-light); }

  .headline { position: absolute; font-weight: 600; line-height: 1.2; color: var(--white); letter-spacing: 0.2px; }
  .site-url { position: absolute; font-weight: 600; font-size: 12px; color: var(--white); }
  .site-url--dark { color: var(--logo-navy); }
  .cta { position: absolute; display: flex; align-items: center; justify-content: center; border: 1.5px solid var(--white); border-radius: 3px; font-family: "Bebas Neue", sans-serif; color: var(--white); letter-spacing: 0.3px; }

  /* Skyscraper */
  .banner--tall { left: 253px; top: 46px; width: 307px; height: 614px; }
  .banner--tall .banner__header { width: 307px; height: 66px; }
  .banner--tall .banner__photo { left: 0; top: 66px; width: 307px; height: 300px; }
  .banner--tall .logo { left: 12px; top: 14px; font-size: 30px; }
  .banner--tall .logo__mark { width: 16px; height: 16px; }
  .banner--tall .headline { left: 0; width: 307px; top: 390px; text-align: center; font-size: 22px; }
  .banner--tall .site-url { left: 0; width: 307px; top: 502px; text-align: center; }
  .banner--tall .cta { left: 71px; top: 534px; width: 165px; height: 38px; font-size: 22px; }

  /* Rectangle */
  .banner--square { left: 613px; top: 337px; width: 390px; height: 323px; }
  .banner--square .banner__header { width: 390px; height: 62px; }
  .banner--square .banner__photo { left: 0; top: 62px; width: 390px; height: 261px; }
  .banner--square .logo { left: 12px; top: 12px; font-size: 30px; }
  .banner--square .logo__mark { width: 16px; height: 16px; }
  .banner--square .headline { left: 24px; top: 278px; font-size: 16px; }
  .banner--square .site-url { left: 223px; top: 248px; }
  .banner--square .cta { left: 223px; top: 281px; width: 155px; height: 36px; font-size: 20px; }

  /* Leaderboard */
  .banner--leader { left: 192px; top: 774px; width: 816px; height: 98px; }
  .banner--leader .banner__header { width: 235px; height: 98px; border-bottom: 0; }
  .banner--leader .banner__photo { left: 235px; top: 0; width: 340px; height: 98px; }
  .banner--leader .logo { left: 10px; top: 33px; font-size: 25px; }
  .banner--leader .logo__mark { width: 14px; height: 14px; }
  .banner--leader .site-url { left: 92px; top: 80px; font-size: 11px; }
  .banner--leader .headline { left: 560px; width: 224px; top: 8px; text-align: center; font-size: 17px; }
  .banner--leader .cta { left: 615px; top: 60px; width: 134px; height: 30px; font-size: 18px; }

  /* Wide leaderboard */
  .banner--wide { left: 34px; top: 940px; width: 1132px; height: 103px; }
  .banner--wide .banner__header { width: 355px; height: 103px; border-bottom: 0; }
  .banner--wide .banner__photo { left: 355px; top: 0; width: 360px; height: 103px; }
  .banner--wide .logo { left: 38px; top: 33px; font-size: 31px; }
  .banner--wide .logo__mark { width: 16px; height: 16px; }
  .banner--wide .site-url { left: 202px; top: 84px; font-size: 11px; }
  .banner--wide .headline { left: 730px; width: 220px; top: 30px; text-align: center; font-size: 19px; }
  .banner--wide .cta { left: 968px; top: 35px; width: 136px; height: 32px; font-size: 19px; }
</style>
</head>
<body>

<section class="banner banner--tall" aria-label="Skyscraper banner">
  <div class="banner__photo" role="img" aria-label="Photo of a smiling group of medical trainees practising CPR on a training manikin"></div>
  <svg class="banner__swoosh" viewBox="0 0 307 614" preserveAspectRatio="none" aria-hidden="true">
    <path d="M0 355 C90 345 200 310 307 250 L307 614 L0 614 Z"/>
  </svg>
  <header class="banner__header">
    <div class="logo">Trainee Panel <span class="logo__mark"></span></div>
  </header>
  <p class="headline">Help a junior doctor<br>make a big decision</p>
  <p class="site-url">www.traineepanel.net</p>
  <div class="cta">Rate your training!</div>
</section>

<section class="banner banner--square" aria-label="Rectangle banner">
  <div class="banner__photo" role="img" aria-label="Photo of a smiling group of medical trainees practising CPR on a training manikin"></div>
  <svg class="banner__swoosh" viewBox="0 0 390 323" preserveAspectRatio="none" aria-hidden="true">
    <path d="M0 268 C150 262 300 200 390 110 L390 323 L0 323 Z"/>
  </svg>
  <header class="banner__header">
    <div class="logo">Trainee Panel <span class="logo__mark"></span></div>
  </header>
  <p class="site-url">www.traineepanel.net</p>
  <p class="headline">Help a junior doctor<br>make a big decision</p>
  <div class="cta">Rate your training!</div>
</section>

<section class="banner banner--leader" aria-label="Leaderboard banner">
  <header class="banner__header">
    <div class="logo">Trainee Panel <span class="logo__mark"></span></div>
    <p class="site-url site-url--dark">www.traineepanel.net</p>
  </header>
  <div class="banner__photo" role="img" aria-label="Photo of a smiling group of medical trainees"></div>
  <svg class="banner__swoosh" viewBox="0 0 816 98" preserveAspectRatio="none" aria-hidden="true">
    <path d="M515 0 C540 30 545 75 575 98 L816 98 L816 0 Z"/>
  </svg>
  <p class="headline">Help a junior doctor<br>make a big decision</p>
  <div class="cta">Rate your training!</div>
</section>

<section class="banner banner--wide" aria-label="Wide leaderboard banner">
  <header class="banner__header">
    <div class="logo">Trainee Panel <span class="logo__mark"></span></div>
    <p class="site-url site-url--dark">www.traineepanel.net</p>
  </header>
  <div class="banner__photo" role="img" aria-label="Photo of a smiling group of medical trainees"></div>
  <svg class="banner__swoosh" viewBox="0 0 1132 103" preserveAspectRatio="none" aria-hidden="true">
    <path d="M650 0 C675 30 680 80 715 103 L1132 103 L1132 0 Z"/>
  </svg>
  <p class="headline">Help a junior doctor<br>make a big decision</p>
  <div class="cta">Rate your training!</div>
</section>

</body>
</html>
```